Create a Poster Campaign for a Zurich-based Crowdfinancing Startup

Company: 9oakvestor GmbH (9ov.ch)
Campaign: First major marketing push
Scope: Billboard posters

Company description:
9oakvestor GmbH is a crowdfinancing platform, where people and businesses needing money can raise funds in three different ways: 1. Crowdlending (borrowing and paying interest), 2. Crowdfactoring for businesses (pre-financing an open invoice), 3. Crowdfunding (rewards-based funding). What 9oakvestor from the competitors differentiates is that borrowers can borrow at their own conditions (amount, duration up to 5 years, and interest rate).
MORE INFO: www.9ov.ch

We are also changing website colours to blue away from brown.

Need:
We need to attract more users to the platform and because we only operate in Switzerland, a poster campaign is meant to create awareness of our brand and services.

We need 2 posters designs in F 200 and F 24 Large Format (Here is a tool to see poster sizes (https://booking.vistaplakat.ch/en/poster-design-tips-and-checklist)

Notes:
We would like to use 9ov.ch as the name and address of the platform. We do not want plant motifs (growth of a plant from dirt, or money growing).

Slogan Ideas:
Too much money? Not enough money? Come to 9OV.

We’ve got your next loan.

Balanced for borrowers and lenders. <— potentially a secondary text block

Target Market(s)

People who need money (businesses and private people) as well as people and businesses looking to invest money. It needs to speak to both.

Industry/Entity Type

Financial

Font styles to use
Serif
Sans Serif

Colors
0355a3
3276b5
85acd3
cedeed

Requirements
Must have
• Message and headline: must get across in 1–2 seconds, be catchy and easy to grasp
• Few words: maximum of ten
• Font size should make text readable up to ten metres
• High contrast dark on light and complementary colours are easiest to take in
• Logo must be clearly recognizable.
• Elements essential to the image, such as texts, should be placed at least 6 cm – in the case of F12 and F24 – and 4 cm – in the case of F4 and F200 formats – from the edge at the top, bottom and sides (this is mandatory in the case of posters placed in light boxes).
Nice to have
• Kivel and Lendra Square have done some creative posters.
Should not have
• No plant images

```html
<!DOCTYPE html>
<html lang="de">
<head>
<meta charset="utf-8">
<title>9oakvestor – Poster</title>
<link rel="stylesheet" href="https://fonts.googleapis.com/css2?family=Oswald:wght@700&family=Montserrat:wght@700&display=swap">
<style>
  :root {
    --paper: #ffffff;
    --navy: #0f4f96;
    --sky: #0fc6f0;
    --brand-brown: #6b4a2b;
    --white: #ffffff;
  }
  html, body {
    margin: 0;
    padding: 0;
    width: 869px;
    height: 1200px;
    overflow: hidden;
    background: var(--paper);
  }
  .poster {
    position: relative;
    width: 869px;
    height: 1200px;
    background: var(--paper);
    overflow: hidden;
  }
  .photo {
    position: absolute;
  }
  .photo--lender {
    left: 54px;
    top: 29px;
    width: 370px;
    height: 530px;
    background: linear-gradient(160deg, #e9ecef 0%, #c9ced4 55%, #a9b6cc 100%);
  }
  .photo--borrower {
    left: 397px;
    top: 466px;
    width: 472px;
    height: 520px;
    background: linear-gradient(200deg, #f3efe9 0%, #e4d8c8 55%, #cdb9a2 100%);
  }
  .brand {
    position: absolute;
    left: 486px;
    top: 92px;
    display: flex;
    align-items: center;
    gap: 14px;
  }
  .brand__dot {
    width: 46px;
    height: 46px;
    border-radius: 50%;
    background: var(--brand-brown);
  }
  .brand__name {
    font-family: "Oswald", sans-serif;
    font-weight: 700;
    font-size: 50px;
    line-height: 1;
    color: var(--brand-brown);
  }
  .headline {
    position: absolute;
    margin: 0;
    font-family: "Oswald", sans-serif;
    font-weight: 700;
    text-transform: uppercase;
    letter-spacing: -1px;
  }
  .headline__line {
    display: block;
    font-size: 132px;
    line-height: 112px;
    height: 112px;
  }
  .headline--surplus {
    right: 28px;
    top: 212px;
    text-align: right;
  }
  .headline--shortage {
    left: 50px;
    top: 556px;
    text-align: left;
  }
  .tone-navy { color: var(--navy); }
  .tone-sky { color: var(--sky); }
  .band {
    position: absolute;
    left: 0;
    width: 869px;
    display: flex;
    align-items: center;
    justify-content: center;
    text-align: center;
    color: var(--white);
  }
  .band--claim {
    top: 986px;
    height: 134px;
    background: var(--navy);
    font-family: "Montserrat", sans-serif;
    font-weight: 700;
    font-size: 37px;
    line-height: 50px;
    letter-spacing: 1px;
  }
  .band--cta {
    top: 1120px;
    height: 80px;
    background: var(--sky);
    font-family: "Oswald", sans-serif;
    font-weight: 700;
    font-size: 42px;
    line-height: 1;
  }
</style>
</head>
<body>
  <main class="poster">
    <div class="photo photo--lender" role="img" aria-label="Smiling businessman in a light grey suit holding out a fan of euro banknotes"></div>
    <div class="photo photo--borrower" role="img" aria-label="Young woman looking worriedly into an empty brown wallet"></div>

    <div class="brand">
      <span class="brand__dot"></span>
      <span class="brand__name">9oakvestor</span>
    </div>

    <h1 class="headline headline--surplus">
      <span class="headline__line tone-navy">Zu viel</span>
      <span class="headline__line tone-sky">Geld?</span>
    </h1>

    <h2 class="headline headline--shortage">
      <span class="headline__line tone-navy">Nicht</span>
      <span class="headline__line tone-navy">genug</span>
      <span class="headline__line tone-sky">Geld?</span>
    </h2>

    <p class="band band--claim" style="margin:0">Der perfekte Ausgleich für<br>Kreditnehmer und Kreditgeber</p>
    <p class="band band--cta" style="margin:0">Besuchen Sie 9ov.ch</p>
  </main>
</body>
</html>
```